Vantrel Consulting Business card design.

See our website www.vantrelconsulting.com which will give you a good idea of what we are about. The font is called 'Play'.

I'd like a standout business card in keeping with the themes and branding on the website

Target Market(s)

professionals. HR directors

Industry/Entity Type

Business

Contact Information for Business Card

Vantrel Consulting PO Box 3917 Marrowdene NSW 2279 1300 584 316 Gareth Lindqvane Principal email: career@vantrelconsulting.com ABN: 41293087614

Other font styles liked:
• Play

Requirements
Must have
• Must have same design colours and branding as website.
• On back I'd prefer a list of the things we do which appears below the name at the header on the website

```html
<!DOCTYPE html>
<html lang="en">
<head>
<meta charset="UTF-8">
<title>Vantrel Consulting – Business Card</title>
<link rel="stylesheet" href="https://fonts.googleapis.com/css2?family=Play:wght@400;700&display=swap">
<style>
  :root {
    --page-bg: #e6e7e9;
    --navy: #0b2239;
    --navy-deep: #071a2d;
    --accent-blue: #2a90d8;
    --name-blue: #3a9be0;
    --card-white: #ffffff;
    --card-grey: #c9cacc;
    --ink: #1c2733;
    --muted: #4a5058;
  }
  * { box-sizing: border-box; margin: 0; padding: 0; }
  html, body {
    width: 1200px; height: 950px; overflow: hidden;
    background: var(--page-bg);
    font-family: "Play", sans-serif;
  }
  .canvas {
    position: relative; width: 1200px; height: 950px;
  }
  .card {
    position: absolute; left: 250px;
    width: 700px; height: 428px;
    overflow: hidden;
    box-shadow: 0 6px 18px rgba(0,0,0,0.18);
  }
  /* back side */
  .card--back {
    top: 35px;
    background: linear-gradient(135deg, var(--card-white) 0%, #ececed 55%, var(--card-grey) 100%);
  }
  .card--back .wordmark {
    position: absolute; left: 0; right: 0; top: 168px;
    text-align: center; font-size: 40px;
  }
  .services {
    position: absolute; right: 70px; top: 240px;
    font-size: 17px; color: var(--muted); letter-spacing: 0.5px;
  }
  .services .sep { margin: 0 8px; }

  .wordmark {
    font-family: "Play", sans-serif; font-weight: 400;
    color: var(--navy); letter-spacing: 3px; text-transform: uppercase;
  }

  /* front side */
  .card--front {
    top: 493px;
    background: linear-gradient(135deg, var(--card-white) 0%, #f1f1f2 60%, #d6d7d9 100%);
  }
  .contact-panel {
    position: absolute; left: 0; top: 0; bottom: 0; width: 318px;
    background: linear-gradient(160deg, var(--navy) 0%, var(--navy-deep) 100%);
    border-right: 4px solid var(--accent-blue);
    padding: 34px 30px;
    color: #fff;
  }
  .person-name {
    font-size: 27px; font-weight: 700; color: var(--name-blue);
  }
  .person-role {
    font-size: 19px; margin-top: 2px;
  }
  .contact-list {
    position: absolute; left: 30px; bottom: 34px; list-style: none;
    font-size: 17px; line-height: 1.35;
  }
  .contact-list li { display: flex; align-items: center; gap: 9px; }
  .contact-list .address { display: block; margin-bottom: 8px; }
  .contact-list svg { width: 17px; height: 17px; flex: none; fill: #fff; }
  .card--front .wordmark {
    position: absolute; left: 318px; right: 0; top: 196px;
    text-align: center; font-size: 29px;
  }
</style>
</head>
<body>
<main class="canvas">

  <section class="card card--back" aria-label="Card back">
    <h1 class="wordmark">Vantrel Consulting</h1>
    <p class="services">Career Coaching<span class="sep">|</span>Leadership<span class="sep">|</span>Outplacement</p>
  </section>

  <section class="card card--front" aria-label="Card front">
    <div class="contact-panel">
      <h2 class="person-name">Gareth Lindqvane</h2>
      <p class="person-role">Principal</p>
      <ul class="contact-list">
        <li class="address">PO Box 3917 Marrowdene<br>NSW 2279</li>
        <li>
          <svg viewBox="0 0 24 24" aria-hidden="true"><path d="M6.6 10.8a15.1 15.1 0 0 0 6.6 6.6l2.2-2.2a1 1 0 0 1 1-.25 11.4 11.4 0 0 0 3.6.57 1 1 0 0 1 1 1V20a1 1 0 0 1-1 1A17 17 0 0 1 3 4a1 1 0 0 1 1-1h3.5a1 1 0 0 1 1 1c0 1.25.2 2.45.57 3.57a1 1 0 0 1-.25 1z"/></svg>
          1300 584 316
        </li>
        <li>
          <svg viewBox="0 0 24 24" aria-hidden="true"><path d="M2 5h20v14H2z M3.5 6.5 12 13l8.5-6.5" fill="#fff" stroke="#0b2239" stroke-width="1.4"/></svg>
          career@vantrelconsulting.com
        </li>
        <li>
          <svg viewBox="0 0 24 24" aria-hidden="true"><circle cx="12" cy="12" r="10"/><path d="M2 12h20M12 2c3 3 3 17 0 20M12 2c-3 3-3 17 0 20" fill="none" stroke="#0b2239" stroke-width="1.4"/></svg>
          www.vantrelconsulting.com
        </li>
      </ul>
    </div>
    <p class="wordmark">Vantrel Consulting</p>
  </section>

</main>
</body>
</html>
```